LUSTRIA INC. is a new Fashion Stylist, Design Merchandiser, and consultant in the fashion industry

We need a logo design for a new Calgary, Alberta based company that is in the business of making over your image, wardrobe and style for both business and personal purposes.

Target Market(s)

Professional female and male business people looking for a new style or complete fashion makeover including clothes closet merchandising and makeover.

Contact Information for Business Card

Number of Pages Required

1 page

Font styles to use
Script

Colors
fac994
fbe7d2
fee3d4

Requirements
Must have
• Fashion Industry theme that is very elegant and colorful using gold/bronze/silver color themes.
Nice to have
• Incorporate the company name with the creative font to come up with the appropriate "logo"

```html
<!DOCTYPE html>
<html lang="en">
<head>
<meta charset="utf-8">
<title>Lustria Inc. Business Card</title>
<link rel="stylesheet" href="https://fonts.googleapis.com/css2?family=Great+Vibes&family=Pinyon+Script&family=Arimo:wght@400&display=swap">
<style>
  :root {
    --backdrop: #e9e8e6;
    --card: #ffffff;
    --peach: #fac994;
    --peach-light: #fbe7d2;
    --blush: #fee3d4;
    --silver: #cfcfd0;
    --silver-soft: #e2e2e3;
    --bronze: #9a5420;
    --rust: #b0601f;
    --ink: #1c1c1c;
  }
  * { margin: 0; padding: 0; box-sizing: border-box; }
  html, body {
    width: 1200px;
    height: 900px;
    overflow: hidden;
    background: var(--backdrop);
  }
  .canvas {
    position: relative;
    width: 1200px;
    height: 900px;
  }
  .card {
    position: absolute;
    width: 600px;
    height: 343px;
    background: var(--card);
    overflow: hidden;
    box-shadow: 0 10px 30px rgba(0, 0, 0, 0.18);
  }
  .card--front { left: 480px; top: 70px; }
  .card--back { left: 120px; top: 470px; }

  .artwork {
    position: absolute;
    inset: 0;
  }
  .card--front .artwork {
    background: radial-gradient(ellipse 70% 85% at 68% 48%,
      var(--blush) 0%,
      var(--peach-light) 30%,
      var(--peach) 60%,
      var(--silver-soft) 85%,
      var(--silver) 100%);
  }
  .card--back .artwork {
    background: radial-gradient(ellipse 80% 100% at 80% 30%,
      var(--card) 0%,
      var(--silver-soft) 70%,
      var(--silver) 100%);
  }

  .logo {
    position: absolute;
    left: 250px;
    top: 130px;
    font-family: "Great Vibes", cursive;
    font-size: 66px;
    line-height: 1;
    color: var(--bronze);
    white-space: nowrap;
  }

  .contact {
    position: absolute;
    left: 70px;
    top: 95px;
  }
  .contact__name {
    font-family: "Pinyon Script", cursive;
    font-size: 44px;
    color: var(--ink);
    line-height: 1.1;
    margin-left: 40px;
  }
  .contact__role {
    font-family: "Arimo", sans-serif;
    font-size: 19px;
    color: var(--rust);
    margin-top: 6px;
  }
  .contact__phone {
    font-family: "Arimo", sans-serif;
    font-size: 20px;
    color: var(--ink);
    margin-top: 8px;
    margin-left: 150px;
  }
</style>
</head>
<body>
<main class="canvas">
  <section class="card card--front" aria-label="Business card front">
    <div class="artwork" role="img" aria-label="Decorative brush-stroke swirl in peach and silver tones"></div>
    <div class="logo">Lustria Inc.</div>
  </section>

  <section class="card card--back" aria-label="Business card back">
    <div class="artwork" role="img" aria-label="Decorative soft silver brush-stroke swirl"></div>
    <div class="contact">
      <p class="contact__name">Marielle Van Hoorst</p>
      <p class="contact__role">Fashion Stylist, Design Merchandiser and consultant</p>
      <p class="contact__phone">403-555-0142</p>
    </div>
  </section>
</main>
</body>
</html>
```